Executive Business Card for Healthcare Company [Need Today]

I need a business card design for a healthcare company. The only branding the company has thus far is a logo. The cards will be utilized by company executives. The design I envision will be vibrant and appealing but with a corporate feel. They shouldn't be too casual or playful. I would like to complete this project TODAY if possible.

Target Market(s)

Healthcare vendors, other executives in healthcare and pharmaceuticals

Industry/Entity Type

Pharmaceutical

Contact Information for Business Card

See attachment

Font styles to use
Serif
Sans Serif

Colors

Designer to choose colors to be used in the design.

```html
<!DOCTYPE html>
<html lang="en">
<head>
<meta charset="utf-8">
<title>Lumera Therapeutics – Executive Business Cards</title>
<link rel="stylesheet" href="https://fonts.googleapis.com/css2?family=Roboto:wght@300;400;700&display=swap">
<style>
  :root {
    --canvas: #cccccc;
    --card: #fbfbfb;
    --teal: #1aabb8;
    --green: #45b48a;
    --divider: #666666;
    --brand: #1fa9b5;
    --ink: #555555;
    --faint: #ececec;
    --white: #ffffff;
  }
  * { box-sizing: border-box; margin: 0; padding: 0; }
  html, body {
    width: 1200px; height: 579px; overflow: hidden;
    background: var(--canvas);
    font-family: "Roboto", Arial, sans-serif;
  }
  .sprites { position: absolute; width: 0; height: 0; }
  .card {
    position: absolute;
    width: 314px; height: 190px;
    border-radius: 12px;
    overflow: hidden;
    background: var(--card);
  }
  .card__watermark {
    position: absolute; left: 0; top: 0;
    width: 314px; height: 190px;
  }
  /* front */
  .card--front {
    background: linear-gradient(180deg, var(--teal) 0%, var(--green) 100%);
  }
  .card--front .brand__name {
    position: absolute; left: 0; right: 0; top: 72px;
    text-align: center;
    font-weight: 300; font-size: 26px; letter-spacing: .5px;
    color: var(--white);
  }
  .card__address {
    position: absolute; left: 0; right: 0; top: 168px;
    text-align: center;
    font-weight: 700; font-size: 9.5px;
    color: var(--white);
  }
  /* contact side */
  .card__band {
    position: absolute; left: 0; top: 0; bottom: 0;
    width: 33px;
    background: linear-gradient(180deg, var(--teal) 0%, var(--green) 100%);
    border-right: 3px solid var(--divider);
  }
  .brand {
    position: absolute; left: 46px; top: 19px;
    display: flex; align-items: center; gap: 10px;
  }
  .brand__dot {
    width: 58px; height: 58px; border-radius: 50%;
    border: 2.5px solid var(--green);
  }
  .brand__name {
    font-weight: 300; font-size: 15px; color: var(--brand);
  }
  .person {
    position: absolute; left: 46px; top: 100px;
  }
  .person__name {
    font-weight: 400; font-size: 14.5px; color: var(--brand);
    line-height: 17px;
  }
  .person__title {
    font-weight: 400; font-size: 7.5px; color: var(--ink);
    margin-top: 3px; min-height: 9px;
  }
  .contact {
    list-style: none; margin-top: 12px;
  }
  .contact li {
    display: flex; align-items: center; gap: 5px;
    font-size: 8px; color: var(--ink); line-height: 11.5px;
  }
  .contact svg { width: 7px; height: 7px; fill: var(--brand); }
</style>
</head>
<body>
<svg class="sprites" aria-hidden="true">
  <defs>
    <symbol id="icon-phone" viewBox="0 0 10 10"><path d="M1 4 Q5 0 9 4 L8 5 L6.5 4 L6.5 3 Q5 2.5 3.5 3 L3.5 4 L2 5 Z M2.5 5.5 H7.5 V9 H2.5 Z"/></symbol>
    <symbol id="icon-mobile" viewBox="0 0 10 10"><path d="M2.5 0.5 H7.5 V9.5 H2.5 Z M3.5 1.5 V7.5 H6.5 V1.5 Z"/></symbol>
    <symbol id="icon-web" viewBox="0 0 10 10"><path d="M5 0.5 A4.5 4.5 0 1 0 5 9.5 A4.5 4.5 0 1 0 5 0.5 Z M1.6 4.5 H8.4 V5.5 H1.6 Z M4.5 1.2 H5.5 V8.8 H4.5 Z" fill-rule="evenodd"/></symbol>
  </defs>
</svg>

<section class="card card--front" style="left:88px;top:84px">
  <svg class="card__watermark" aria-hidden="true"><circle cx="170" cy="95" r="118" fill="none" stroke="rgba(255,255,255,.14)" stroke-width="6"/></svg>
  <p class="brand__name">Lumera Therapeutics</p>
  <p class="card__address">118 W Maple Ave &nbsp;|&nbsp; Dalton GA 30720</p>
</section>

<section class="card card--contact" style="left:445px;top:84px">
  <div class="card__band"></div>
  <svg class="card__watermark" aria-hidden="true"><circle cx="243" cy="120" r="82" fill="none" stroke="var(--faint)" stroke-width="8"/></svg>
  <div class="brand"><span class="brand__dot"></span><span class="brand__name">Lumera Therapeutics</span></div>
  <div class="person">
    <h2 class="person__name">Mark Ellison</h2>
    <p class="person__title">President &amp; CEO</p>
    <ul class="contact">
      <li><svg><use href="#icon-phone"/></svg>855-310-4400 x150</li>
      <li><svg><use href="#icon-mobile"/></svg>404-555-0142</li>
      <li><svg><use href="#icon-web"/></svg>mellison@lumerarx.com</li>
    </ul>
  </div>
</section>

<section class="card card--contact" style="left:798px;top:84px">
  <div class="card__band"></div>
  <svg class="card__watermark" aria-hidden="true"><circle cx="243" cy="120" r="82" fill="none" stroke="var(--faint)" stroke-width="8"/></svg>
  <div class="brand"><span class="brand__dot"></span><span class="brand__name">Lumera Therapeutics</span></div>
  <div class="person">
    <h2 class="person__name">Ray Dunmore</h2>
    <p class="person__title">Chief Financial Officer</p>
    <ul class="contact">
      <li><svg><use href="#icon-phone"/></svg>855-310-4400 x125</li>
      <li><svg><use href="#icon-mobile"/></svg>678-555-0188</li>
      <li><svg><use href="#icon-web"/></svg>rdunmore@lumerarx.com</li>
    </ul>
  </div>
</section>

<section class="card card--contact" style="left:88px;top:304px">
  <div class="card__band"></div>
  <svg class="card__watermark" aria-hidden="true"><circle cx="243" cy="120" r="82" fill="none" stroke="var(--faint)" stroke-width="8"/></svg>
  <div class="brand"><span class="brand__dot"></span><span class="brand__name">Lumera Therapeutics</span></div>
  <div class="person">
    <h2 class="person__name">Owen Pratt</h2>
    <p class="person__title">Senior Director of Marketing</p>
    <ul class="contact">
      <li><svg><use href="#icon-phone"/></svg>864-555-0131</li>
      <li><svg><use href="#icon-mobile"/></svg>864-555-0129</li>
      <li><svg><use href="#icon-web"/></svg>opratt@lumerarx.com</li>
    </ul>
  </div>
</section>

<section class="card card--contact" style="left:445px;top:304px">
  <div class="card__band"></div>
  <svg class="card__watermark" aria-hidden="true"><circle cx="243" cy="120" r="82" fill="none" stroke="var(--faint)" stroke-width="8"/></svg>
  <div class="brand"><span class="brand__dot"></span><span class="brand__name">Lumera Therapeutics</span></div>
  <div class="person">
    <h2 class="person__name">Neil Castor</h2>
    <p class="person__title"></p>
    <ul class="contact">
      <li><svg><use href="#icon-phone"/></svg>855-310-4400 x127</li>
      <li><svg><use href="#icon-mobile"/></svg>706-555-0113</li>
      <li><svg><use href="#icon-web"/></svg>ncastor@lumerarx.com</li>
    </ul>
  </div>
</section>

<section class="card card--contact" style="left:798px;top:304px">
  <div class="card__band"></div>
  <svg class="card__watermark" aria-hidden="true"><circle cx="243" cy="120" r="82" fill="none" stroke="var(--faint)" stroke-width="8"/></svg>
  <div class="brand"><span class="brand__dot"></span><span class="brand__name">Lumera Therapeutics</span></div>
  <div class="person">
    <h2 class="person__name">Glen Morrow</h2>
    <p class="person__title">Chief Operations Officer</p>
    <ul class="contact">
      <li><svg><use href="#icon-phone"/></svg>855-310-4400 x152</li>
      <li><svg><use href="#icon-mobile"/></svg>931-555-0144</li>
      <li><svg><use href="#icon-web"/></svg>gmorrow@lumerarx.com</li>
    </ul>
  </div>
</section>
</body>
</html>
```